Marlow Crest Group (Real Estate and Investment)

A high end, clean design.
We are a real estate company with sales, asset management and investment divisions. We want to use a black and white scheme which is really high end feel. The back of the card can just be the logo (black background with the white writing) as we will probably emboss this when we print)

Target Market(s)

High level investors, high end houses for sale

Industry/Entity Type

Business

Contact Information for Business Card

Name, position, phone number and email address
Glen Varley, Managing Director, 0437259064 and glen@marlowcrest-example.com.au

Requirements
Must have
• Back of the card to be the black background with the white writing (as per the attached images). Would like the capacity to emboss the writing and logo

```html
<!DOCTYPE html>
<html lang="en">
<head>
<meta charset="utf-8">
<title>Marlow Crest Group – Business Card</title>
<link href="https://fonts.googleapis.com/css2?family=Work+Sans:wght@400&family=Didact+Gothic&family=Open+Sans:wght@400&display=swap" rel="stylesheet">
<style>
  :root {
    --page-bg: #e9e7e4;
    --card-black: #231f20;
    --card-white: #f8f8f6;
    --ink-black: #1b1b1b;
    --ink-white: #ffffff;
    --rule: #3a3a3a;
    --shadow: rgba(0, 0, 0, 0.22);
  }
  * { box-sizing: border-box; margin: 0; padding: 0; }
  html, body {
    width: 1200px;
    height: 1200px;
    overflow: hidden;
    background: var(--page-bg);
  }
  .sheet {
    width: 1200px;
    height: 1200px;
    display: flex;
    flex-direction: column;
    align-items: center;
    justify-content: center;
    gap: 60px;
  }
  .card {
    width: 840px;
    height: 480px;
    border-radius: 22px;
    box-shadow: 0 14px 30px var(--shadow);
    position: relative;
  }
  .card--back { background: var(--card-black); }
  .card--front { background: var(--card-white); }

  .wordmark {
    position: absolute;
    left: 0;
    right: 0;
    display: flex;
    align-items: center;
    justify-content: center;
    gap: 22px;
    font-family: "Work Sans", sans-serif;
    font-weight: 400;
    letter-spacing: 1px;
    text-transform: uppercase;
  }
  .wordmark__dot {
    border-radius: 50%;
    border: 2px solid currentColor;
  }
  .card--back .wordmark {
    top: 190px;
    color: var(--ink-white);
    font-size: 50px;
  }
  .card--back .wordmark__dot { width: 48px; height: 48px; }
  .card--front .wordmark {
    top: 110px;
    color: var(--ink-black);
    font-size: 40px;
  }
  .card--front .wordmark__dot { width: 38px; height: 38px; }

  .contact-row {
    position: absolute;
    left: 60px;
    right: 40px;
    top: 310px;
    display: flex;
    align-items: flex-start;
    color: var(--ink-black);
  }
  .contact-item {
    display: flex;
    align-items: flex-start;
    gap: 8px;
    padding: 0 22px;
  }
  .contact-item:first-child { padding-left: 0; }
  .contact-item + .contact-item { border-left: 1.5px solid var(--rule); min-height: 92px; }
  .contact-item svg { flex: none; margin-top: 4px; }
  .person__name {
    font-family: "Didact Gothic", sans-serif;
    font-size: 30px;
    line-height: 1.1;
    letter-spacing: 1px;
  }
  .person__role {
    font-family: "Didact Gothic", sans-serif;
    font-size: 15px;
    margin-top: 6px;
    letter-spacing: 0.5px;
  }
  .contact-text {
    font-family: "Open Sans", sans-serif;
    font-size: 15px;
    line-height: 1.3;
  }
  .contact-item--email .contact-text { font-size: 14px; }
</style>
</head>
<body>
<main class="sheet">
  <section class="card card--back" aria-label="Card back">
    <div class="wordmark"><span class="wordmark__dot"></span><span>Marlow Crest Group</span></div>
  </section>

  <section class="card card--front" aria-label="Card front">
    <div class="wordmark"><span class="wordmark__dot"></span><span>Marlow Crest Group</span></div>

    <div class="contact-row">
      <div class="contact-item contact-item--person">
        <svg width="18" height="22" viewBox="0 0 18 22" aria-hidden="true">
          <circle cx="9" cy="6" r="5" fill="#1b1b1b"/>
          <path d="M1 21 C1 14 4 12 9 12 C14 12 17 14 17 21 Z" fill="#1b1b1b"/>
        </svg>
        <div>
          <div class="person__name">Glen Varley</div>
          <div class="person__role">Managing Director</div>
        </div>
      </div>

      <div class="contact-item contact-item--phone">
        <svg width="18" height="18" viewBox="0 0 24 24" aria-hidden="true">
          <path d="M6.6 10.8a15.1 15.1 0 0 0 6.6 6.6l2.2-2.2a1 1 0 0 1 1-.25 11.4 11.4 0 0 0 3.6.57 1 1 0 0 1 1 1V20a1 1 0 0 1-1 1A17 17 0 0 1 3 4a1 1 0 0 1 1-1h3.5a1 1 0 0 1 1 1c0 1.25.2 2.45.57 3.6a1 1 0 0 1-.25 1z" fill="#1b1b1b"/>
        </svg>
        <span class="contact-text">0437259064</span>
      </div>

      <div class="contact-item contact-item--email">
        <svg width="20" height="15" viewBox="0 0 20 15" aria-hidden="true">
          <rect x="0" y="0" width="20" height="15" fill="#1b1b1b"/>
          <path d="M1 1 L10 8 L19 1" stroke="#f8f8f6" stroke-width="1.6" fill="none"/>
        </svg>
        <span class="contact-text">glen@marlowcrest-example.com.au</span>
      </div>
    </div>
  </section>
</main>
</body>
</html>
```